Produktblatt für Anbieter von Nahrungsergänzungsmitteln
Zielgruppe
Nahrungsergänzungsmittel für medizinische Zwecke, insbesondere in Pulver- und Pastillenform auf
pflanzlicher Basis mit Getreide- und Kräuterinhaltsstoffen
Mehlmischung zum Kochen und Backen, Nudeln, Teig, Teigwaren, Kuchen, Torten, usw.
Aufgabenstellung
Naturverbundenheit, Logo, font Avenir Next LT Pro, ansprechend online und ausgedruckt, textliche Inhalte

```html
<!DOCTYPE html>
<html lang="de">
<head>
<meta charset="utf-8">
<title>Produktdatenblatt Presslinge</title>
<link href="https://fonts.googleapis.com/css2?family=Nunito+Sans:wght@400;600;700;800;900&display=swap" rel="stylesheet">
<style>
:root{
  --bg:#f1f1f1;
  --paper:#ffffff;
  --orange:#f59d0c;
  --head:#c3e0aa;
  --row:#e1edd5;
  --head-text:#1d560d;
  --text:#3b3b3b;
  --accent:#3f9a2a;
  --badge-a:#6cc12e;
  --badge-b:#2f9424;
}
*{margin:0;padding:0;box-sizing:border-box}
html,body{width:1200px;height:1200px;overflow:hidden;background:var(--bg);font-family:"Nunito Sans",sans-serif;color:var(--text)}
.sheet{position:absolute;left:225px;top:46px;width:749px;height:1090px;background:var(--paper);box-shadow:0 6px 24px rgba(0,0,0,.12);overflow:hidden}
.sheet-title{position:absolute;left:73px;top:88px;font-size:31px;font-weight:900;color:var(--orange);letter-spacing:.3px}
.title-rule{position:absolute;left:0;top:134px;width:204px;height:5px;background:var(--orange)}
.data-table{position:absolute;left:67px;width:620px;border-collapse:collapse;table-layout:fixed;font-size:12.5px;z-index:2}
.data-table td,.data-table th{border:1.5px solid #fff;padding:0 3px;text-align:left;vertical-align:middle;font-weight:400;white-space:nowrap;overflow:hidden}
.data-table .head th{background:var(--head);color:var(--head-text);font-weight:700;font-size:14px;height:30px}
.data-table td{background:var(--row);height:28px}
.data-table .center{text-align:center}
.data-table .sub td{font-weight:700}
.data-table .sub td.plain{font-weight:400}
.t-product{top:164px}
.t-storage{top:303px}
.t-dose{top:490px}
.t-ingredients{top:576px}
.t-values{top:662px}
.t-dose td,.t-ingredients td{height:29px}
.t-values td{height:27px}
.footnote{position:absolute;left:69px;top:782px;font-size:10.5px;color:var(--text);white-space:nowrap;z-index:3}
.stand{position:absolute;left:75px;top:810px;font-size:9.5px;font-weight:800;color:var(--accent);letter-spacing:.3px}
.meadow{position:absolute;left:0;top:902px;width:749px;height:188px;background:linear-gradient(160deg,#5f8a2a 0%,#3d6a1c 35%,#2f5716 60%,#4a7a22 100%)}
.couple{position:absolute;left:560px;top:758px;width:189px;height:332px;background:linear-gradient(180deg,#c9a37f 0%,#8d6a4d 35%,#7d8a9a 70%,#a9b8c8 100%);border-radius:80px 50px 0 0;z-index:1}
.badge{position:absolute;left:383px;top:826px;width:150px;height:150px;border-radius:50%;background:linear-gradient(160deg,var(--badge-a),var(--badge-b));color:#fff;text-align:center;display:flex;flex-direction:column;justify-content:center;z-index:2}
.badge-main{font-size:24px;font-weight:900;line-height:1.1}
.badge-sub{font-size:14px;font-weight:700;line-height:1.2}
</style>
</head>
<body>
<main class="sheet">
  <h1 class="sheet-title">PRODUKTDATENBLATT</h1>
  <div class="title-rule"></div>

  <table class="data-table t-product">
    <colgroup><col style="width:189px"><col></colgroup>
    <tr class="head"><th>Produkt</th><th class="center">Presslinge 150 | 500</th></tr>
    <tr><td>Verkehrsbezeichnung</td><td>Nahrungsergänzungsmittel mit Vitamin C (Ascorbinsäure)</td></tr>
    <tr><td>Inverkehrbringer</td><td>Halmwerk Gesundheit GmbH, Lindenweg 4, A-1010 Wien</td></tr>
    <tr><td>Packungsgrösse (PZN)</td><td>150 Tabletten (PZN-9999999) | 500 Tabletten (PZN-9999999)</td></tr>
  </table>

  <table class="data-table t-storage">
    <colgroup><col style="width:189px"><col></colgroup>
    <tr class="head"><th colspan="2">Füllmenge &amp; Lagerungsbedingungen</th></tr>
    <tr><td>Nettofüllmenge</td><td>120 g (150 Tabletten) | 400 g (500 Tabletten)</td></tr>
    <tr><td>Lagerungstemperatur</td><td>Zimmertemperatur und vor Sonneneinstrahlung geschützt lagern</td></tr>
    <tr><td>Lagerungsbedingungen</td><td>Außerhalb der Reichweite von Kindern aufbewahren</td></tr>
    <tr><td>Angabeformat des MHD</td><td>MM / JJJJ</td></tr>
    <tr><td>Laufzeit</td><td>36 Monate</td></tr>
  </table>

  <table class="data-table t-dose">
    <tr class="head"><th>Dosierungs-Vorschlag</th></tr>
    <tr><td>3 x täglich 5 Stück mit Wasser zerkauen (ca. 20 Min. vor den Mahlzeiten) oder 8 Stück zwischendurch.</td></tr>
  </table>

  <table class="data-table t-ingredients">
    <tr class="head"><th>Zutaten</th></tr>
    <tr><td>Khorasan-Weizen (Korvana®), Dinkel, Sorbit, 10% Schafgarbenkraut, 5% Ginko, Vitamin C (Ascorbinsäure)</td></tr>
  </table>

  <table class="data-table t-values">
    <colgroup><col style="width:187px"><col style="width:193px"><col></colgroup>
    <tr class="head"><th colspan="3">Wertbestimmende Zutaten</th></tr>
    <tr class="sub"><td>Stoff</td><td>Pro Presslinge</td><td class="plain">% NRV*</td></tr>
    <tr><td>Selen</td><td>?</td><td>?</td></tr>
    <tr><td>Vitamin C (Ascorbinsäure)</td><td>?</td><td>?</td></tr>
  </table>
  <p class="footnote">* Nährstoffbezugswerte (NRV) für die tägliche Zufuhr gemäss Lebensmittelinformationsverordnung</p>
  <p class="stand">STAND: 01.2024</p>

  <div class="meadow" role="img" aria-label="Foto einer grünen Wiese mit gelben Blumen"></div>
  <div class="couple" role="img" aria-label="Foto eines lachenden jungen Paares im Freien"></div>
  <div class="badge">
    <span class="badge-main">Vitalität</span>
    <span class="badge-sub">in jeder<br>Lebensphase.</span>
  </div>
</main>
</body>
</html>
```